Elegant YET Modern - Business Card Design

I need a business card for my real estate consulting business. I am hired by developers to create and manage marketing and sales programs for their high-end, multi-unit real estate developments. These projects can last a few years. My clients are fast-moving, affluent, no nonsense men (mostly). I need a card that is elegant yet modern, understated yet with a creative touch. Less is more! Colors need to be sophisticated...charcoal grey/white or I'm open.
I would like my tagline: "Elevate Your Real Estate. Accelerate Your Sales." on the back of card with a simple skyline illustration (hopefully I can get the skyline spot colored)...see attached sample
I don't have a logo yet so simple clean chic is good start. I D NOT want a bunch of "Stars" in a row as too predictable. But an interesting treatment of stars in or around logo type could be great.
The FINAL design should communicate: modern elegance, confidence, and restraint

Target Market(s)

affluent male real estate developers between 45-70 - confident, succesful, busy, results oriented

Industry/Entity Type

Real Estate

Contact Information for Business Card

Bright Harbor Promotions
Elevate Your Real Estate. Accelerate Your Sales.

Lorna Whitfield
President
314.727.9081
Lorna@brightharborpromo.com

Requirements
Must have
• The name "Bright Harbor Promotions" is a play on the star rating system for hotels and resorts...(and indicates the types of projects I work on) ...if there is a Star or Stars in your design (and I would love it) the treatment of the Star/s should imply sophistication (either modern or understated)...but not contrived or cheap looking.

I also like the idea of a reference to real estate...can be the simple skyline rendering but I'm open to other suggestions...should NOT BE a single home or roof top as I DO NOT sell single family residential homes...I AM NOT a real estate agent!!!

```html
<!DOCTYPE html>
<html lang="en">
<head>
<meta charset="utf-8">
<title>Bright Harbor Promotions – Business Card</title>
<link rel="stylesheet" href="https://fonts.googleapis.com/css2?family=Open+Sans:wght@400;600&family=Arimo:wght@400;700&display=swap">
<style>
  :root {
    --charcoal: #584a48;
    --charcoal-deep: #443836;
    --gold: #d4b062;
    --white: #ffffff;
    --ink: #111111;
    --page: #ffffff;
  }
  html, body {
    margin: 0;
    padding: 0;
    width: 1200px;
    height: 1000px;
    overflow: hidden;
    background: var(--page);
  }
  .canvas {
    position: relative;
    width: 1200px;
    height: 1000px;
    font-family: "Open Sans", sans-serif;
  }
  .wordmark {
    position: absolute;
    margin: 0;
    font-family: "Open Sans", sans-serif;
    font-weight: 400;
    white-space: nowrap;
    letter-spacing: -0.2px;
  }

  /* Logo card on charcoal */
  .logo-card {
    position: absolute;
    left: 124px;
    top: 12px;
    width: 466px;
    height: 267px;
    box-sizing: border-box;
    background: var(--charcoal);
    border: 1px solid #2f2625;
  }
  .logo-card .wordmark {
    left: 0;
    right: 0;
    top: 112px;
    text-align: center;
    font-size: 30px;
    color: var(--white);
  }

  /* Logo on white */
  .logo-standalone {
    left: 645px;
    top: 122px;
    font-size: 33px;
    color: var(--charcoal);
  }

  /* Front of card */
  .card-front {
    position: absolute;
    left: 62px;
    top: 315px;
    width: 589px;
    height: 346px;
    background: var(--white);
    box-shadow: -6px 8px 14px rgba(0,0,0,0.45);
  }
  .divider {
    position: absolute;
    left: 294px;
    top: 89px;
    width: 2px;
    height: 168px;
    background: var(--gold);
  }
  .identity {
    position: absolute;
    right: 302px;
    top: 149px;
    text-align: right;
    font-family: "Arimo", sans-serif;
    font-size: 16px;
    line-height: 20px;
    color: var(--ink);
  }
  .identity .name { font-weight: 700; }
  .contact {
    position: absolute;
    left: 301px;
    top: 149px;
    font-family: "Arimo", sans-serif;
    font-size: 16px;
    line-height: 20px;
    color: var(--ink);
    letter-spacing: 0.3px;
  }
  .sparkle {
    position: absolute;
    border-radius: 50%;
    background: var(--gold);
  }
  .sparkle.lg { width: 12px; height: 12px; }
  .sparkle.md { width: 9px; height: 9px; }
  .sparkle.sm { width: 7px; height: 7px; }

  /* Back of card */
  .card-back {
    position: absolute;
    left: 551px;
    top: 577px;
    width: 601px;
    height: 351px;
    background: var(--charcoal);
    box-shadow: -6px 8px 14px rgba(0,0,0,0.45);
    overflow: hidden;
  }
  .skyline {
    position: absolute;
    left: 0;
    bottom: 0;
    width: 601px;
    height: 351px;
    background: linear-gradient(180deg, var(--charcoal) 0%, var(--charcoal-deep) 70%, var(--charcoal-deep) 100%);
  }
  .card-back .wordmark {
    left: 48px;
    top: 72px;
    font-size: 26px;
    color: var(--white);
  }
  .tagline {
    position: absolute;
    left: 0;
    right: 0;
    top: 296px;
    margin: 0;
    text-align: center;
    font-size: 15.5px;
    color: var(--white);
  }
  .tagline .accent { color: var(--gold); }
</style>
</head>
<body>
<main class="canvas">

  <section class="logo-card" aria-label="Logo on charcoal">
    <p class="wordmark">Bright Harbor Promotions</p>
  </section>

  <p class="wordmark logo-standalone">Bright Harbor Promotions</p>

  <section class="card-front" aria-label="Card front">
    <span class="sparkle lg" style="left:365px; top:33px;"></span>
    <span class="sparkle md" style="left:336px; top:66px;"></span>
    <span class="sparkle md" style="left:500px; top:74px;"></span>
    <span class="sparkle sm" style="left:535px; top:42px;"></span>
    <span class="sparkle sm" style="left:532px; top:106px;"></span>
    <div class="identity">
      <div class="name">Lorna Whitfield</div>
      <div class="title">President</div>
    </div>
    <div class="divider"></div>
    <div class="contact">
      <div class="phone">314.727.9081</div>
      <div class="email">Lorna@brightharborpromo.com</div>
    </div>
  </section>

  <section class="card-back" aria-label="Card back">
    <div class="skyline" role="img" aria-label="Silhouette of a city skyline with high-rise towers"></div>
    <span class="sparkle lg" style="left:373px; top:34px;"></span>
    <span class="sparkle md" style="left:344px; top:67px;"></span>
    <span class="sparkle sm" style="left:546px; top:43px;"></span>
    <span class="sparkle md" style="left:510px; top:75px;"></span>
    <span class="sparkle sm" style="left:543px; top:108px;"></span>
    <p class="wordmark">Bright Harbor Promotions</p>
    <p class="tagline"><span class="accent">Elevate</span> Your Real Estate. <span class="accent">Accelerate</span> Your Sales.</p>
  </section>

</main>
</body>
</html>
```